Veterinary Clinic Letterhead - Ridgeview Veterinary Surgery

We need a letterhead design for an established Veterinary Clinic in Mareeba called Ridgeview Veterinary Surgery. We are a moderate sized mixed animal veterinary clinic offering a wide variety of veterinary services. The design should use the same colour pattern as those in the logos supplied. The design should also include our address (48 Tulloch Road, Mareeba, Queensland, 4880), phone number (07 4158 6734), email (admin@ridgeviewvets.com.au), website (www.ridgeviewvets.com.au) and our opening hours (8am to 5pm Monday to Friday and 8am to 12pm Saturday).
Target Market(s)
Pet owners
Industry/Entity Type
Veterinary
Requirements
Must have
- The logo or modification of it, business address, opening hours, website, phone number and email address

```html
<!DOCTYPE html>
<html lang="en">
<head>
<meta charset="utf-8">
<title>Ridgeview Veterinary Surgery – Letterhead</title>
<link href="https://fonts.googleapis.com/css2?family=Arimo:wght@400;700&display=swap" rel="stylesheet">
<style>
  :root {
    --backdrop: #595959;
    --paper: #ffffff;
    --header-tint: #cddff0;
    --wave-mid: #1a7ec6;
    --wave-deep: #0a55a8;
    --ink: #111111;
    --brand-navy: #1d3d6e;
    --watermark: #c8d0da;
  }
  * { box-sizing: border-box; margin: 0; padding: 0; }
  html, body { width: 900px; height: 1200px; overflow: hidden; }
  body { background: var(--backdrop); font-family: "Arimo", Arial, sans-serif; position: relative; }

  .letterhead {
    position: absolute; left: 82px; top: 118px; width: 735px; height: 948px;
    background: var(--paper); overflow: hidden;
    box-shadow: 0 4px 14px rgba(0,0,0,0.45);
  }
  .header-waves { position: absolute; left: 0; top: 0; width: 735px; height: 290px; }

  .contact-list { position: absolute; left: 22px; top: 18px; list-style: none; }
  .contact-item {
    display: flex; align-items: center; gap: 8px;
    font-weight: 700; font-size: 21px; color: var(--ink); height: 30px;
    white-space: nowrap;
  }
  .contact-icon { width: 20px; height: 20px; flex: none; }
  .opening-hours {
    position: absolute; left: 51px; top: 141px;
    font-weight: 700; font-size: 19px; line-height: 25px; color: var(--ink);
    white-space: nowrap;
  }
  .opening-hours .saturday { padding-left: 79px; display: block; }

  .brand-mark { position: absolute; right: 14px; top: 16px; width: 200px; text-align: center; }
  .brand-circle {
    width: 90px; height: 90px; border-radius: 50%;
    background: var(--brand-navy); margin: 0 auto 8px;
  }
  .brand-name {
    font-weight: 700; font-size: 14px; line-height: 17px; color: var(--brand-navy);
    white-space: nowrap;
  }

  .watermark { position: absolute; left: 0; top: 426px; width: 735px; text-align: center; }
  .watermark-circle {
    width: 188px; height: 188px; border-radius: 50%;
    background: var(--watermark); opacity: 0.7; margin: 0 auto 20px;
  }
  .watermark-name {
    font-weight: 700; font-size: 32px; line-height: 36px; color: var(--watermark);
    white-space: nowrap;
  }
</style>
</head>
<body>
  <main class="letterhead">
    <svg class="header-waves" viewBox="0 0 735 290" aria-hidden="true">
      <path fill="var(--header-tint)" d="M0 0 H735 V200 C650 160 520 165 420 205 S150 250 0 190 Z"/>
      <path fill="var(--wave-mid)" d="M0 190 C150 250 300 255 420 205 S650 160 735 200 V232 C650 195 520 200 420 232 S150 272 0 200 Z"/>
      <path fill="var(--wave-deep)" d="M0 200 C150 272 300 262 420 232 S650 195 735 232 V277 C650 232 520 228 420 256 S150 292 0 215 Z"/>
    </svg>

    <ul class="contact-list">
      <li class="contact-item">
        <svg class="contact-icon" viewBox="0 0 20 20" aria-hidden="true"><path d="M10 1a6 6 0 0 0-6 6c0 4.5 6 10 6 10s6-5.5 6-10a6 6 0 0 0-6-6zm0 8.5A2.5 2.5 0 1 1 10 4.5a2.5 2.5 0 0 1 0 5z" fill="none" stroke="#111" stroke-width="2"/><path d="M5 18.5h10" stroke="#111" stroke-width="1.5"/></svg>
        <span>48 Tulloch Road,Kelvale,Westmoor,4892</span>
      </li>
      <li class="contact-item">
        <svg class="contact-icon" viewBox="0 0 20 20" aria-hidden="true"><path d="M5 2l3 4-2 2c1 2 3 4 5 5l2-2 4 3-2 3C9 17 3 11 2 5z" fill="#111"/></svg>
        <span>07 4158 6734</span>
      </li>
      <li class="contact-item">
        <svg class="contact-icon" viewBox="0 0 20 20" aria-hidden="true"><rect x="1" y="4" width="18" height="12" fill="#111"/><path d="M1 4l9 7 9-7" fill="none" stroke="#fff" stroke-width="1.5"/></svg>
        <span>admin@ridgeviewvets.com.au</span>
      </li>
      <li class="contact-item">
        <svg class="contact-icon" viewBox="0 0 20 20" aria-hidden="true"><g fill="none" stroke="#111" stroke-width="1.4"><circle cx="10" cy="10" r="8.5"/><ellipse cx="10" cy="10" rx="4" ry="8.5"/><path d="M1.5 10h17M3 5.5h14M3 14.5h14M10 1.5v17"/></g></svg>
        <span>www.ridgeviewvets.com.au</span>
      </li>
    </ul>

    <p class="opening-hours">Opens: Monday- Friday (8am-5pm)<span class="saturday">Saturday (8am-12pm)</span></p>

    <div class="brand-mark">
      <div class="brand-circle"></div>
      <p class="brand-name">RIDGEVIEW VETERINARY<br>SURGERY</p>
    </div>

    <div class="watermark">
      <div class="watermark-circle"></div>
      <p class="watermark-name">RIDGEVIEW VETERINARY<br>SURGERY</p>
    </div>
  </main>
</body>
</html>
```